Yoga Studio Postcard Advertising Flyer

Need a postcard size flyer that will promote our business. The objective is to promote location and availability. Want it to be personal. The objective to connect the audience to the purpose of yoga and the focus on enabling functional well-being. Something that is a very big focus at this point in time in the world. I really want people to see the value in connecting with us via our website, calmora app, pagewell or vibro. The colours are to be bright but not overwhelming and aligned to the logo colours. Its also important to have the location picture on the flyer - unless you think that it is way too much (try a with or without). I don't want this to be a specials brochure - it is an introduction to our brand and our business. No need to over do it with promotional lines apart from come and join us.

Delayed in organising this.

Local yogis and residence who are or want to be focused on well-being.

• Pictures - would have the logo on one side.
• Modern and aligned to website design.

```html
<!DOCTYPE html>
<html lang="en">
<head>
<meta charset="utf-8">
<title>Amber Reed Yoga – Postcard Flyer</title>
<link rel="stylesheet" href="https://fonts.googleapis.com/css2?family=Arimo:wght@400;600;700&display=swap">
<style>
  :root {
    --page-bg: #ffffff;
    --card-bg: #b4dfeb;
    --accent-circle: #93d2e4;
    --ink: #1f2a33;
    --body-ink: #2f3a42;
    --brand-blue: #1f6f9f;
    --social-navy: #1d3f6e;
    --panel-white: #ffffff;
    --photo-light: #d9d4cc;
    --photo-mid: #b59a7c;
  }
  * { margin: 0; padding: 0; box-sizing: border-box; }
  html, body {
    width: 1200px;
    height: 1066px;
    overflow: hidden;
    background: var(--page-bg);
    font-family: "Arimo", Arial, sans-serif;
  }
  .flyer {
    position: absolute;
    left: 274px;
    top: 72px;
    width: 643px;
    height: 905px;
    background: var(--card-bg);
    overflow: hidden;
  }
  .accent-circle {
    position: absolute;
    left: -12px;
    top: -12px;
    width: 394px;
    height: 394px;
    border-radius: 50%;
    background: var(--accent-circle);
  }
  .headline {
    position: absolute;
    left: 51px;
    top: 50px;
    font-weight: 700;
    font-size: 41px;
    line-height: 47px;
    color: var(--ink);
    letter-spacing: 0.5px;
  }
  .intro {
    position: absolute;
    left: 51px;
    top: 196px;
    width: 440px;
    font-size: 16.5px;
    line-height: 20.5px;
    color: var(--body-ink);
  }
  .brand {
    position: absolute;
    left: 430px;
    top: 38px;
    width: 190px;
    text-align: center;
    color: var(--brand-blue);
    font-weight: 600;
    font-size: 24px;
    line-height: 26px;
    letter-spacing: 0.5px;
  }
  .brand-dot {
    display: block;
    width: 54px;
    height: 54px;
    margin: 0 auto 34px;
    border-radius: 50%;
    background: var(--brand-blue);
  }
  .brand-sub {
    display: block;
    font-size: 15px;
    letter-spacing: 6px;
  }
  .studio-photo {
    position: absolute;
    left: 125px;
    top: 314px;
    width: 381px;
    height: 381px;
    border-radius: 50%;
    background: radial-gradient(circle at 50% 40%, var(--photo-light) 0%, var(--photo-mid) 100%);
  }
  .vision {
    position: absolute;
    left: 46px;
    top: 679px;
    width: 300px;
    color: var(--ink);
  }
  .vision-rule {
    width: 125px;
    height: 0;
    border: none;
    border-top: 2px solid var(--ink);
    margin-bottom: 12px;
  }
  .vision-title {
    font-weight: 600;
    font-size: 20px;
    line-height: 24px;
  }
  .vision-text {
    width: 270px;
    font-size: 15.5px;
    line-height: 20px;
    color: var(--body-ink);
  }
  .vision-cta {
    font-weight: 700;
    font-size: 15.5px;
    line-height: 20px;
  }
  .social {
    position: absolute;
    left: 471px;
    top: 700px;
    list-style: none;
  }
  .social-item {
    display: flex;
    align-items: center;
    height: 34px;
    font-size: 14px;
    color: var(--ink);
  }
  .social-mark {
    width: 27px;
    height: 27px;
    border-radius: 50%;
    background: var(--social-navy);
    margin-right: 10px;
    flex: none;
  }
  .contact-panel {
    position: absolute;
    left: 55px;
    top: 812px;
    width: 507px;
    height: 58px;
    border-radius: 10px;
    background: var(--panel-white);
    text-align: center;
    color: var(--ink);
  }
  .contact-url {
    margin-top: 8px;
    font-weight: 700;
    font-size: 20px;
    line-height: 24px;
  }
  .contact-address {
    font-size: 13px;
    line-height: 18px;
  }
</style>
</head>
<body>
  <main class="flyer">
    <div class="accent-circle"></div>

    <h1 class="headline">ENABLE<br>FUNCTIONAL<br>WELLBEING</h1>

    <p class="intro">Strengthen your well-being through adaptive yoga. Seek to evolve your mind and body through the challenge of yoga. Perfection is a desire and never an outcome through the practice of yoga.</p>

    <div class="brand">
      <span class="brand-dot"></span>
      AMBER REED
      <span class="brand-sub">YOGA</span>
    </div>

    <div class="studio-photo" role="img" aria-label="Photo of the studio hall with white walls, arched windows, a wooden floor and rows of blue yoga mats in sunlight"></div>

    <section class="vision">
      <hr class="vision-rule">
      <h2 class="vision-title">Our vision</h2>
      <p class="vision-text">is to create an atmosphere that enables inclusiveness of the whole community.</p>
      <p class="vision-cta">Come join us!</p>
    </section>

    <ul class="social">
      <li class="social-item"><span class="social-mark"></span>amberreedyoga</li>
      <li class="social-item"><span class="social-mark"></span>amberreed</li>
      <li class="social-item"><span class="social-mark"></span>amberreed</li>
    </ul>

    <footer class="contact-panel">
      <p class="contact-url">www.amberreedyoga.com.au</p>
      <p class="contact-address">THE CHAPEL, 214 HARBOUR LANE ELWOOD NSW 2077</p>
    </footer>
  </main>
</body>
</html>
```